IT solutions & services company requires stationary makeover

Looking for a consistent modern, professional design across our printed client touch points:
Business Cards
Letterhead
Client proposal
Flyer
Postcard

We provide solutions for SME IT - servers, backups, AV etc, and the ongoing services around them.
we are happy with our logo - please see attached and would like the colour theme to be maintained.

```html
<!DOCTYPE html>
<html lang="en">
<head>
<meta charset="utf-8">
<title>Corvix – Presentation Folder</title>
<link href="https://fonts.googleapis.com/css2?family=Montserrat:wght@400;500&display=swap" rel="stylesheet">
<style>
  :root {
    --backdrop: #e9e9e7;
    --brand-blue: #1f6f95;
    --brand-deep: #175b7d;
    --brand-light: #5fb6e0;
    --paper: #ffffff;
    --paper-shade: #efefef;
    --ink-light: #eaf4fa;
  }
  * { margin: 0; padding: 0; box-sizing: border-box; }
  html, body { width: 1200px; height: 801px; overflow: hidden; }
  body {
    position: relative;
    background: var(--backdrop);
    font-family: "Montserrat", Arial, sans-serif;
  }

  /* Folder outside */
  .folder-cover {
    position: absolute;
    left: 47px; top: 29px;
    width: 573px; height: 409px;
    background: linear-gradient(180deg, #2479a2 0%, var(--brand-blue) 55%, var(--brand-deep) 100%);
    box-shadow: 0 3px 10px rgba(0,0,0,.25);
    overflow: hidden;
  }
  .cover-fibre-art {
    position: absolute;
    left: 0; top: 0;
    width: 400px; height: 409px;
    background:
      radial-gradient(ellipse at 0% 35%, rgba(120,200,240,.55) 0%, rgba(80,170,220,.25) 40%, rgba(31,111,149,0) 75%);
  }
  .cover-fold {
    position: absolute;
    left: 287px; top: 0;
    width: 1px; height: 100%;
    background: rgba(0,0,0,.12);
  }
  .cover-brand {
    position: absolute;
    left: 290px; top: 206px;
    width: 240px;
  }
  .brand-name {
    display: flex;
    align-items: center;
    gap: 14px;
    color: var(--paper);
    font-weight: 400;
    font-size: 52px;
    line-height: 1;
    letter-spacing: 1px;
  }
  .brand-dot {
    width: 40px; height: 40px;
    border-radius: 50%;
    background: var(--brand-light);
    flex: none;
  }
  .brand-tagline {
    margin-top: 6px;
    padding-left: 54px;
    color: var(--ink-light);
    font-size: 11px;
    font-weight: 400;
    letter-spacing: .6px;
    text-transform: uppercase;
  }
  .cover-contact {
    position: absolute;
    left: 40px; top: 364px;
    width: 240px;
    text-align: center;
    color: var(--ink-light);
    font-style: italic;
    font-size: 6.5px;
    line-height: 9px;
  }

  /* Folder inside */
  .folder-inside {
    position: absolute;
    left: 575px; top: 357px;
    width: 572px; height: 403px;
    background: linear-gradient(90deg, var(--paper) 0%, #f7f7f7 40%, #e8e8e8 50%, var(--paper) 51%, #f6f6f6 100%);
    box-shadow: 0 3px 10px rgba(0,0,0,.2);
  }
  .inside-pocket {
    position: absolute;
    left: 285px; top: 0;
    width: 287px; height: 403px;
  }
  .pocket-art { position: absolute; left: 0; bottom: 0; }
  .card-slot {
    position: absolute;
    left: 21px; top: 335px;
    width: 113px; height: 60px;
    background: var(--paper);
  }
  .pocket-brand {
    position: absolute;
    left: 157px; top: 344px;
  }
  .pocket-brand .brand-name { font-size: 22px; gap: 6px; letter-spacing: .5px; }
  .pocket-brand .brand-dot { width: 16px; height: 16px; }
  .pocket-brand .brand-tagline { font-size: 5px; padding-left: 22px; margin-top: 3px; }
</style>
</head>
<body>

<section class="folder-cover" aria-label="Folder outside">
  <div class="cover-fibre-art" role="img" aria-label="Glowing blue fibre-optic strands fanning out from the left edge"></div>
  <div class="cover-fold"></div>

  <div class="cover-brand">
    <div class="brand-name"><span class="brand-dot"></span>Corvix</div>
    <div class="brand-tagline">Your Solution Partner</div>
  </div>

  <address class="cover-contact">
    03 555 0172<br>
    hello@corvix.example<br>
    Level 2, Harbour Lane, Riverton, NZ<br>
    www.corvix.example
  </address>
</section>

<section class="folder-inside" aria-label="Folder inside">
  <div class="inside-pocket">
    <svg class="pocket-art" width="287" height="130" viewBox="0 0 287 130" aria-hidden="true">
      <defs>
        <linearGradient id="pocketFill" x1="0" y1="0" x2="1" y2="0">
          <stop offset="0" stop-color="#14536f"/>
          <stop offset="1" stop-color="#1f6f95"/>
        </linearGradient>
      </defs>
      <path d="M0 38 C 90 38, 200 30, 287 0 L 287 130 L 0 130 Z" fill="url(#pocketFill)"/>
    </svg>
    <div class="card-slot" aria-label="Business card slot"></div>
    <div class="pocket-brand">
      <div class="brand-name"><span class="brand-dot"></span>Corvix</div>
      <div class="brand-tagline">Your Solution Partner</div>
    </div>
  </div>
</section>

</body>
</html>
```